New Woocommerce Design Project

We need a WooCommerce site design that reflects our personality as a young and stylish teenage 'athleisure' fashion brand. Our target market is young boys aged between 12 and 18 years old, who are sporty, cool, and fashion conscious. We would like to the site to feature large format photos of our products and models, as well as feature pages for product selection for purchase. This is a new company we are launching, so we are looking for a dynamic yet stylish design which is quick and easy to navigate and which will appeal to young people. We already have a logo which we will upload below. Our existing domain name is www.orbitwren.com. We would like the winning designer to code the website - if possible. We have uploaded some photos of the products currently being manufactured so you can see the type of design/style.

Target Market(s)

Teenage boys

Industry/Entity Type

Fashion

Coding

Coded - Design and coding required

Colors

Designer to choose colors to be used in the design.

Requirements
Must have
• Inclusion of logo, design must be stylish and contemporary. Colours must include white, logo background colour, and a dark navy blue.
Nice to have
• Inclusion of whole page photos of possible
Should not have
• Nothing that looks cheap or too childish.

```html
<!DOCTYPE html>
<html lang="en">
<head>
<meta charset="utf-8">
<title>Orbitwren – Teenage Athleisure Fashion</title>
<link rel="stylesheet" href="https://fonts.googleapis.com/css2?family=Poppins:wght@300;400;500&display=swap">
<style>
:root{
  --navy:#1e1c2f;
  --navy-deep:#16142a;
  --navy-field:#262439;
  --taupe:#8c7f77;
  --ink:#1f1e29;
  --muted:#5a5862;
  --white:#ffffff;
  --line:#3a3850;
}
*{margin:0;padding:0;box-sizing:border-box}
html,body{width:1200px;height:4508px;overflow:hidden}
body{position:relative;background:var(--white);font-family:"Poppins",sans-serif;color:var(--ink)}
.abs{position:absolute}
a{color:inherit;text-decoration:none}

/* header */
.site-header{left:0;top:0;width:1200px;height:62px;background:var(--white)}
.brand{left:88px;top:14px;font-size:30px;font-weight:400;letter-spacing:5px;color:var(--taupe);display:flex;align-items:center;gap:12px}
.brand-dot{width:16px;height:16px;border-radius:50%;background:var(--taupe)}
.main-nav{left:438px;top:22px;display:flex;gap:34px;font-size:12px;font-weight:500;letter-spacing:.3px}
.cart-btn{left:1006px;top:14px;width:104px;height:34px;background:var(--taupe);color:var(--white);font-size:12px;display:flex;align-items:center;justify-content:center;gap:6px;clip-path:polygon(12px 0,100% 0,calc(100% - 12px) 100%,0 100%)}

/* hero */
.hero-bg{left:0;top:62px}
.hero-photo{left:255px;top:125px;width:520px;height:660px;border-radius:45% 45% 30% 30%;background:radial-gradient(ellipse at 50% 40%,#7d6a57 0%,#4b4042 45%,rgba(30,28,47,0) 72%)}
.hero-tag{left:85px;top:428px;font-size:30px;line-height:37px;color:var(--white);font-weight:400}
.hero-title{left:695px;top:415px;font-size:124px;font-weight:400;color:var(--white);letter-spacing:2px;line-height:1}
.shop-now{left:922px;top:555px;width:188px;height:52px;background:var(--taupe);color:var(--white);font-size:17px;display:flex;align-items:center;justify-content:center;gap:10px;clip-path:polygon(18px 0,100% 0,calc(100% - 18px) 100%,0 100%)}

/* categories */
.cat-photo-left{left:88px;top:900px;width:332px;height:505px;clip-path:polygon(0 9%,100% 0,100% 91%,0 100%);background:linear-gradient(160deg,#3a4a74 0%,#1d2a52 55%,#2a2a30 100%)}
.cat-photo-right{left:775px;top:768px;width:333px;height:487px;clip-path:polygon(0 9%,100% 0,100% 91%,0 100%);background:linear-gradient(150deg,#9ea3a6 0%,#5d6064 50%,#2c2d31 100%)}
.cat-heading{left:430px;top:898px;width:340px;text-align:center;font-size:42px;line-height:46px;font-weight:400}
.cat-list{left:430px;top:1012px;width:340px;list-style:none;text-align:center;font-size:24px;line-height:35.7px}
.cat-list .is-out{color:var(--taupe);text-decoration:line-through}
.cat-all{left:430px;top:1250px;width:320px;text-align:center;font-size:15px;color:var(--taupe);text-decoration:underline;text-underline-offset:4px}

/* promo tiles */
.promo-tiles{left:0;top:1234px;width:1200px;height:617px;clip-path:polygon(0 43%,100% 0,100% 100%,0 100%)}
.tile{position:absolute;top:0;height:617px;width:400px}
.tile-sale{left:0;background:linear-gradient(135deg,#8a8d93 0%,#2c3550 50%,#9fa1a5 100%)}
.tile-new{left:400px;background:linear-gradient(150deg,#8f9092 0%,#3d3d40 55%,#a8a28e 100%)}
.tile-hot{left:800px;background:linear-gradient(160deg,#6b6f74 0%,#b8bcc2 45%,#2c3458 100%)}
.tile-num{position:absolute;left:58px;top:455px;font-size:62px;color:var(--white);line-height:1}
.tile-sub{position:absolute;left:58px;top:530px;font-size:25px;color:var(--white);line-height:1}

/* popular collections */
.popular-heading{left:0;top:1985px;width:1200px;text-align:center;font-size:42px;font-weight:400}
.product{top:2068px;height:400px}
.p1{left:88px;width:150px;background:linear-gradient(180deg,#6d6e72,#3a3b3f 60%,#8c8d90)}
.p2{left:246px;width:176px;background:linear-gradient(180deg,#b9bbbe,#5e6064 55%,#2a2d3c)}
.p3{left:433px;width:334px;background:linear-gradient(160deg,#9b9893,#55555a 55%,#6f6c67)}
.p4{left:777px;width:333px;background:linear-gradient(180deg,#e7e7e5,#c9cacb 50%,#8b8c90)}
.p5{left:1120px;width:80px;background:linear-gradient(180deg,#efe9e2,#9b8a7c 70%,#3b342f)}
.cart-tag{top:2106px;width:64px;height:24px;background:var(--navy);color:var(--white);font-size:10px;display:flex;align-items:center;justify-content:center;gap:4px;clip-path:polygon(8px 0,100% 0,calc(100% - 8px) 100%,0 100%)}
.carousel-next{left:1097px;top:2235px;width:50px;height:50px;border-radius:50%;border:2px solid var(--ink);background:var(--white);display:flex;align-items:center;justify-content:center}

/* about */
.about-title{left:84px;top:2645px;font-size:88px;line-height:84px;font-weight:400}
.about-copy{left:89px;top:2836px;width:510px;font-size:15.5px;line-height:25px;color:var(--muted)}
.read-more{left:88px;top:3005px;width:188px;height:54px;background:var(--taupe);color:var(--white);font-size:17px;display:flex;align-items:center;justify-content:center;clip-path:polygon(16px 0,100% 0,calc(100% - 16px) 100%,0 100%)}
.about-model{left:745px;top:2535px;width:170px;height:620px;border-radius:60px 60px 20px 20px;background:linear-gradient(180deg,#b7a89b 0%,#6b6b70 25%,#3b3b40 55%,#1f1f24 90%,#d8d8d8 100%)}

/* video band */
.dark-base{left:0;top:3135px}
.video-photo{left:0;top:3135px;width:1200px;height:800px;clip-path:polygon(0 17%,100% 0,100% 100%,0 78%);background:linear-gradient(100deg,#2b2a30 0%,#8b8c8f 25%,#55565c 45%,#1e2438 65%,#a2a3a6 78%,#1e1c2f 100%)}
.video-title{left:360px;top:3410px;font-size:112px;line-height:108px;color:var(--white);font-weight:400}
.play-btn{left:990px;top:3480px;width:120px;height:120px;border-radius:50%;background:var(--taupe);display:flex;align-items:center;justify-content:center}

/* newsletter */
.news-heading{left:0;top:3970px;width:1200px;text-align:center;font-size:36px;color:var(--white);font-weight:400}
.news-form{left:265px;top:4037px;width:668px;height:60px;background:var(--navy-field);display:flex;align-items:center;justify-content:space-between;padding:0 32px}
.news-form .placeholder{font-size:16px;color:var(--white)}
.news-form .submit{font-size:12px;color:var(--taupe);display:flex;align-items:center;gap:8px}

/* footer */
.foot-brand{left:88px;top:4244px;font-size:38px;letter-spacing:6px;color:var(--white);display:flex;align-items:center;gap:16px}
.foot-brand .brand-dot{width:22px;height:22px}
.foot-col{top:4185px;color:var(--white)}
.foot-col h3{font-size:20px;font-weight:400;margin-bottom:8px}
.foot-col ul{list-style:none;font-size:13px;line-height:28px;padding-left:2px}
.col-company{left:458px}
.col-legal{left:683px}
.col-contact{left:917px}
.col-contact li{display:flex;align-items:center;gap:7px}
.socials{display:flex;gap:14px;margin-top:8px}
.socials span{width:12px;height:12px;border-radius:50%;background:var(--white)}
.to-top{left:1125px;top:4400px;width:40px;height:40px;border-radius:50%;background:var(--taupe);display:flex;align-items:center;justify-content:center}
.foot-rule{left:88px;top:4445px;width:1022px;height:1px;background:var(--line)}
.copyright{left:0;top:4469px;width:1200px;text-align:center;font-size:13px;color:var(--white)}
</style>
</head>
<body>

<header class="site-header abs">
  <div class="brand abs"><span class="brand-dot"></span>ORBITWREN</div>
  <nav class="main-nav abs">
    <a href="#">OUR COLLECTIONS</a><a href="#">ABOUT US</a><a href="#">CONTACT US</a>
  </nav>
  <a class="cart-btn abs" href="#">
    <svg width="12" height="12" viewBox="0 0 12 12" fill="none" stroke="#fff" stroke-width="1.2"><rect x="2" y="4" width="8" height="7"/><path d="M4 4V3a2 2 0 0 1 4 0v1"/></svg>Cart</a>
</header>

<section class="hero">
  <svg class="hero-bg abs" width="1200" height="805" viewBox="0 0 1200 805"><polygon points="0,0 1200,0 1200,612 0,804" fill="var(--navy)"/></svg>
  <div class="hero-photo abs" role="img" aria-label="Teen model leaping in black tee, tan joggers and trainers"></div>
  <p class="hero-tag abs">LISH TEENAGE<br>'ATHLEISURE'<br>FASHION</p>
  <h1 class="hero-title abs">BRAND</h1>
  <a class="shop-now abs" href="#">SHOP NOW
    <svg width="16" height="10" viewBox="0 0 16 10" fill="none" stroke="#fff" stroke-width="1.3"><path d="M0 5h15M11 1l4 4-4 4"/></svg></a>
</section>

<section class="categories">
  <div class="cat-photo-left abs" role="img" aria-label="Model from behind in navy hoodie with shopping bag"></div>
  <div class="cat-photo-right abs" role="img" aria-label="Model in cap, bomber jacket and black shorts against a wall"></div>
  <h2 class="cat-heading abs">SHOP BY<br>CATEGORIES</h2>
  <ul class="cat-list abs">
    <li>SHIRTS</li><li>PANTS</li><li class="is-out">TROUSERS</li><li>SUITS</li><li>JACKETS</li><li>BELTS</li>
  </ul>
  <a class="cat-all abs" href="#">VIEW ALL CATEGORIES</a>
</section>

<section class="promo-tiles abs">
  <div class="tile tile-sale" role="img" aria-label="Model in navy varsity sweatshirt and grey joggers">
    <span class="tile-num">30%</span><span class="tile-sub">FLAT SALE</span></div>
  <div class="tile tile-new" role="img" aria-label="Athlete stretching in training shorts and running shoes">
    <span class="tile-num">NEW</span><span class="tile-sub">ARRIVAL PRODUCTS</span></div>
  <div class="tile tile-hot" role="img" aria-label="Model in grey sweatshirt and navy trousers">
    <span class="tile-num">HOT</span><span class="tile-sub">TSHIRT SALE</span></div>
</section>

<section class="popular">
  <h2 class="popular-heading abs">POPULAR COLLECTIONS</h2>
  <div class="product p1 abs" role="img" aria-label="Grey sweatshirt with dark joggers"></div>
  <div class="product p2 abs" role="img" aria-label="Quilted grey jacket with navy joggers"></div>
  <div class="product p3 abs" role="img" aria-label="Model seated in grey long-sleeve top and shorts"></div>
  <div class="product p4 abs" role="img" aria-label="White tee with grey joggers"></div>
  <div class="product p5 abs" role="img" aria-label="Model carrying a leather holdall"></div>
  <a class="cart-tag abs" style="left:78px" href="#"><svg width="9" height="9" viewBox="0 0 12 12" fill="none" stroke="#fff" stroke-width="1.4"><rect x="2" y="4" width="8" height="7"/><path d="M4 4V3a2 2 0 0 1 4 0v1"/></svg>Cart</a>
  <a class="cart-tag abs" style="left:423px" href="#"><svg width="9" height="9" viewBox="0 0 12 12" fill="none" stroke="#fff" stroke-width="1.4"><rect x="2" y="4" width="8" height="7"/><path d="M4 4V3a2 2 0 0 1 4 0v1"/></svg>Cart</a>
  <a class="cart-tag abs" style="left:768px" href="#"><svg width="9" height="9" viewBox="0 0 12 12" fill="none" stroke="#fff" stroke-width="1.4"><rect x="2" y="4" width="8" height="7"/><path d="M4 4V3a2 2 0 0 1 4 0v1"/></svg>Cart</a>
  <a class="carousel-next abs" href="#" aria-label="Next"><svg width="12" height="16" viewBox="0 0 12 16" fill="none" stroke="#1f1e29" stroke-width="2"><path d="M3 2l6 6-6 6"/></svg></a>
</section>

<section class="about">
  <h2 class="about-title abs">ABOUT<br>ORBITWREN</h2>
  <p class="about-copy abs">Lorem Ipsum is simply dummy text of the printing and typesetting industry. Lorem Ipsum has been the industry's standard dummy text ever since the 1500s, when an unknown printer took a galley of type and scrambled it to make a type specimen book. It has survived not only five centuries, but also the leap into electronic typesetting.</p>
  <a class="read-more abs" href="#">READ MORE</a>
  <div class="about-model abs" role="img" aria-label="Model in grey cowl-neck knit, black joggers and white trainers"></div>
</section>

<svg class="dark-base abs" width="1200" height="1373" viewBox="0 0 1200 1373"><polygon points="0,136 1200,0 1200,1373 0,1373" fill="var(--navy)"/></svg>
<section class="video">
  <div class="video-photo abs" role="img" aria-label="Two models in grey tee and navy hooded jacket"></div>
  <h2 class="video-title abs">ORBITWREN<br>FASHION</h2>
  <a class="play-btn abs" href="#" aria-label="Play video"><svg width="40" height="44" viewBox="0 0 40 44"><polygon points="4,2 38,22 4,42" fill="#fff"/></svg></a>
</section>

<section class="newsletter">
  <h2 class="news-heading abs">SUBSCRIBE TO OUR NEWSLETTER</h2>
  <form class="news-form abs">
    <span class="placeholder">Enter your email</span>
    <span class="submit">SUBSCRIBE <svg width="14" height="9" viewBox="0 0 16 10" fill="none" stroke="#8c7f77" stroke-width="1.4"><path d="M0 5h15M11 1l4 4-4 4"/></svg></span>
  </form>
</section>

<footer>
  <div class="foot-brand abs"><span class="brand-dot"></span>ORBITWREN</div>
  <div class="foot-col col-company abs"><h3>COMPANY</h3>
    <ul><li>About Us</li><li>Services</li><li>Why Us</li><li>Testimonial</li><li>Case Studies</li></ul></div>
  <div class="foot-col col-legal abs"><h3>LEGAL</h3>
    <ul><li>All Products</li><li>Solutions</li><li>Our Products</li><li>Team Members</li></ul></div>
  <div class="foot-col col-contact abs"><h3>CONTACT</h3>
    <ul>
      <li><svg width="9" height="12" viewBox="0 0 9 12"><path d="M4.5 0A4.5 4.5 0 0 0 0 4.5C0 8 4.5 12 4.5 12S9 8 9 4.5A4.5 4.5 0 0 0 4.5 0zm0 6.3a1.8 1.8 0 1 1 0-3.6 1.8 1.8 0 0 1 0 3.6z" fill="#8c7f77"/></svg>12 Harbour Lane, Leeds</li>
      <li><svg width="11" height="8" viewBox="0 0 11 8" fill="none" stroke="#8c7f77"><rect x=".5" y=".5" width="10" height="7"/><path d="M.5.5l5 4 5-4"/></svg>info@orbitwren.com</li>
      <li><svg width="10" height="10" viewBox="0 0 10 10" fill="none" stroke="#8c7f77"><circle cx="5" cy="5" r="4.5"/><path d="M.5 5h9M5 .5c2 2.5 2 6.5 0 9M5 .5c-2 2.5-2 6.5 0 9"/></svg>www.orbitwren.com</li>
    </ul>
    <div class="socials"><span></span><span></span><span></span><span></span></div>
  </div>
  <a class="to-top abs" href="#" aria-label="Back to top"><svg width="10" height="7" viewBox="0 0 10 7" fill="none" stroke="#fff" stroke-width="1.4"><path d="M1 6l4-4 4 4"/></svg></a>
  <div class="foot-rule abs"></div>
  <p class="copyright abs">Copyright Orbitwren 2023 | All Rights Reserved</p>
</footer>

</body>
</html>
```